Flier redesign

Sample fliers are attached from previous 2 years "Seasonal care 2018" and "2019 Seasonal Care" . Need an updated design for this year.

Possible images are attached to this brief. If you use the before/after pictures - you should use both of them. Use images attached to this brief or any from our website that you may prefer.

Colors

Designer to choose colors to be used in the design.

Requirements
Must have
• Colors should match our website theme. www.oakmerefieldgrounds.org
• Should be a "new" design, not just copying one of the prior year designs with a different image.
• Must be created in photoshop and file must be provided at the end.
• Text should be the same as 2019 version.

```html
<!DOCTYPE html>
<html lang="en">
<head>
<meta charset="utf-8">
<title>2019 Landscaping Packages – Oakmere Field Grounds</title>
<link rel="stylesheet" href="https://fonts.googleapis.com/css2?family=Montserrat:ital,wght@0,400;0,500;0,600;0,700;0,800;1,600;1,700;1,800;1,900&display=swap">
<style>
  :root {
    --backdrop: #9b1a1e;
    --brand-red: #a8161d;
    --brand-red-dark: #8a0f15;
    --ink: #222222;
    --card-white: #f2f1f0;
    --paper: #ffffff;
    --gold-light: #f3d77a;
    --gold-dark: #c99a1e;
    --leaf-light: #a9c46a;
    --leaf-dark: #3f5a22;
    --lawn: #8fb55a;
  }
  * { box-sizing: border-box; margin: 0; padding: 0; }
  html, body { width: 1200px; height: 1000px; overflow: hidden; }
  body {
    background: var(--backdrop);
    font-family: "Montserrat", sans-serif;
    color: var(--ink);
    position: relative;
  }
  .flyer {
    position: absolute;
    left: 230px; top: 20px;
    width: 740px; height: 960px;
    background: var(--paper);
    overflow: hidden;
    box-shadow: 0 10px 30px rgba(0,0,0,.35);
  }
  .hero-photo {
    position: absolute; inset: 0 0 55px 0;
    background:
      linear-gradient(180deg, rgba(0,0,0,0) 55%, rgba(225,225,225,.85) 85%, #dcdcdc 100%),
      linear-gradient(180deg, var(--leaf-light) 0%, #7a9a45 22%, var(--leaf-dark) 38%, #c9ccc6 48%, var(--lawn) 62%, #9cbf6a 75%);
  }
  .brand-tag {
    position: absolute; left: 63px; top: 0;
    width: 76px; height: 97px;
    background: var(--paper);
    display: flex; flex-direction: column; align-items: center; justify-content: flex-end;
    padding-bottom: 14px; gap: 6px;
  }
  .brand-tag .mark { width: 22px; height: 22px; border-radius: 50%; background: var(--brand-red); }
  .brand-tag .name {
    font-size: 10px; font-weight: 600; color: var(--brand-red);
    text-align: center; line-height: 1.15; text-transform: uppercase;
  }
  .title-band { position: absolute; left: 0; top: 0; width: 740px; height: 500px; }
  .title {
    position: absolute; left: 80px; top: 300px;
    transform: rotate(-5deg); transform-origin: left top;
  }
  .title .year-line {
    font-size: 36px; font-weight: 800; color: var(--ink);
    margin-left: 84px; letter-spacing: .5px; line-height: 1;
  }
  .title .headline {
    font-size: 104px; font-weight: 900; font-style: italic; color: var(--brand-red);
    line-height: .95; letter-spacing: -1px;
  }
  .card {
    position: absolute; width: 220px;
    background: var(--card-white);
    border-radius: 30px 30px 40px 40px;
    overflow: hidden;
    display: flex; flex-direction: column;
    box-shadow: 0 2px 6px rgba(0,0,0,.12);
  }
  .card-head {
    background: linear-gradient(180deg, var(--brand-red) 0%, var(--brand-red-dark) 100%);
    color: #fff; text-align: center;
    font-style: italic; font-weight: 800; text-transform: uppercase;
    line-height: 1;
  }
  .card-sub {
    color: var(--brand-red); font-style: italic; font-weight: 700;
    font-size: 12px; text-align: center; line-height: 1.05;
    padding: 6px 8px; border-bottom: 1px solid var(--brand-red);
  }
  .card-body { padding: 10px 10px 0; font-size: 9.6px; line-height: 1.45; }
  .card-body p { margin-bottom: 1px; }
  .card-body .season { color: var(--brand-red); font-weight: 700; font-size: 11px; }
  .price-bar {
    background: linear-gradient(180deg, var(--brand-red) 0%, var(--brand-red-dark) 100%);
    color: #fff; font-style: italic; font-weight: 800; text-align: center;
  }
  .card-foot { text-align: center; color: var(--brand-red-dark); font-style: italic; font-weight: 700; }
  .card-foot small { display: block; font-size: 7.5px; }
  .card-foot strong { display: block; font-size: 13px; font-weight: 800; }

  .card--season { left: 18px; top: 575px; height: 308px; }
  .card--season .card-head { font-size: 19px; padding: 13px 0 9px; }
  .card--season .card-body { height: 70px; }
  .card--season .price-bar { font-size: 20px; height: 36px; line-height: 36px; margin-top: 3px; }
  .card--season .card-foot { padding-top: 7px; }

  .card--basic { left: 250px; top: 580px; height: 310px; }
  .card--basic .card-head { font-size: 14px; padding: 8px 0 5px; }
  .card--basic .card-head span { display: block; font-size: 19px; }
  .card--basic .card-body { height: 150px; padding-top: 20px; }

  .card--perpetual { left: 488px; top: 535px; height: 360px; }
  .card--perpetual .card-head { font-size: 15px; padding: 8px 0 5px; }
  .card--perpetual .card-head span { display: block; font-size: 19px; }
  .card--perpetual .card-body { height: 200px; padding-top: 18px; }

  .card--basic .price-bar, .card--perpetual .price-bar { font-size: 30px; height: 40px; line-height: 40px; }
  .card--basic .card-foot, .card--perpetual .card-foot { padding-top: 9px; }
  .card .monthly { font-size: 11px; font-weight: 500; padding: 0 14px 8px; }

  .popular-badge {
    position: absolute; left: 520px; top: 487px; width: 220px; height: 41px;
    background: linear-gradient(180deg, var(--gold-light) 0%, var(--gold-dark) 100%);
    border-radius: 22px 0 0 0;
    color: #fff; font-style: italic; font-weight: 800; font-size: 17px;
    text-align: center; line-height: 41px; letter-spacing: .5px;
    text-shadow: 0 1px 2px rgba(0,0,0,.35);
  }
  .contact-strip {
    position: absolute; left: 0; bottom: 0; width: 100%; height: 55px;
    background: var(--paper);
    font-size: 12px; font-weight: 500; padding: 18px 0 0 24px;
  }
</style>
</head>
<body>
  <article class="flyer">
    <div class="hero-photo" role="img" aria-label="Sunlit cemetery grounds with rows of headstones, trees and green lawn"></div>

    <div class="brand-tag">
      <span class="mark"></span>
      <span class="name">Oakmere<br>Field<br>Grounds</span>
    </div>

    <svg class="title-band" viewBox="0 0 740 500" aria-hidden="true">
      <polygon points="0,317 740,267 740,427 0,478" fill="rgba(240,240,240,.8)"/>
    </svg>

    <h1 class="title">
      <div class="year-line">2019 LANDSCAPING</div>
      <div class="headline">PACKAGES</div>
    </h1>

    <section class="card card--season">
      <h2 class="card-head">Season Care</h2>
      <div class="card-sub">Seasonal landscaping<br>grave care</div>
      <div class="card-body">
        <p>| Weeding and trimming services on your gravesite approximately every 7 weeks during the growing season:</p>
        <p class="season">mid-April through mid-October</p>
      </div>
      <div class="price-bar">3 years | $345</div>
      <div class="price-bar">2 years| $230</div>
      <div class="price-bar">1 year | $115</div>
      <div class="card-foot">
        <small>Multi-year payment locks in current rates</small>
        <strong>Valid through 10/31/2019</strong>
      </div>
    </section>

    <section class="card card--basic">
      <h2 class="card-head">Basic Care<span>Endowment</span></h2>
      <div class="card-sub">Landscaping care forever<br>for graves with no plantings</div>
      <div class="card-body">
        <p>| Weeding and trimming services on your gravesite 2 times per year:</p>
        <p class="season">mid-May and mid-September</p>
        <p>| Monument leveling</p>
        <p>| Payment ensures grave care forever</p>
      </div>
      <p class="monthly">12 monthly payments of</p>
      <div class="price-bar">$239</div>
      <div class="card-foot">
        <small>Call for single payment discount.</small>
        <strong>Valid through 10/31/2019</strong>
      </div>
    </section>

    <div class="popular-badge">MOST POPULAR</div>

    <section class="card card--perpetual">
      <h2 class="card-head">Perpetual Care<span>Endowment</span></h2>
      <div class="card-sub">Landscaping care forever<br>for graves with plantings</div>
      <div class="card-body">
        <p>| Weeding and triming services on your gravesite approximately every 7 weeks during the growing season:</p>
        <p class="season">mid - April trough mid-October</p>
        <p>| Monument leveling and cleanig</p>
        <p>| Payment ensures grave care forever</p>
        <p>| Full bed of boxwood shrubs</p>
        <p>| Replacement shrubs</p>
        <p>| Trust certificate</p>
      </div>
      <p class="monthly">12 monthly payments of</p>
      <div class="price-bar">$297</div>
      <div class="card-foot">
        <small>Call for single payment discount.</small>
        <strong>Valid through 10/31/2019</strong>
      </div>
    </section>

    <footer class="contact-strip">info@oakmerefieldgrounds.org | (201) 555-0148 | www.oakmerefieldgrounds.org</footer>
  </article>
</body>
</html>
```